Design von Drucksorten for Wedding Invitation Cards

I need a Wedding Invitation Card. The couple has given me 78 pictures of their time together over the years and we did an Engagement Shooting as well. They want sort of a mosaic with the 78 pictures (or some) as well as have some pictures of the engagement shooting (as i shot those - they should be larger! :) ) in the card.

I want an indesign file so i can change the text and maybe change some pictures at their will.

I usually have square cards (21x21cm or 15x15cm) that are folded once (open 15x30 and 21x42) but am open to other suggestions as well.

Here are the files:
http://fy.zq/PmRtXoBL31d

```html
<!DOCTYPE html>
<html lang="en">
<head>
<meta charset="utf-8">
<title>Owen &amp; Lucia – Wedding Invitation</title>
<link href="https://fonts.googleapis.com/css2?family=Great+Vibes&family=Open+Sans:wght@400;700&display=swap" rel="stylesheet">
<style>
  :root{
    --page:#ecebe8;
    --card-edge:#b9b9b9;
    --card-mid:#d9d9d9;
    --card-light:#f2f2f2;
    --rim:#ffffff;
    --ink:#2b2b2b;
    --ink-soft:#444;
    --photo-dark:#2c3a4e;
    --photo-warm:#b89a7a;
    --photo-light:#d8c2a2;
  }
  *{margin:0;padding:0;box-sizing:border-box}
  html,body{width:1200px;height:749px;overflow:hidden;background:var(--page)}
  .canvas{position:relative;width:1200px;height:749px}
  .card{
    position:absolute;left:200px;width:800px;
    background:radial-gradient(ellipse at 55% 50%,var(--card-light) 0%,var(--card-mid) 65%,var(--card-edge) 100%);
    box-shadow:0 6px 18px rgba(0,0,0,.18);
    overflow:hidden;
  }
  .pocket-card{top:40px;height:290px}
  .invitation-card{top:375px;height:335px}
  .card svg{position:absolute;inset:0}
  .invite-text{
    position:absolute;left:470px;top:20px;width:310px;
    text-align:center;color:var(--ink);
    font-family:"Open Sans",sans-serif;
  }
  .couple-names{
    font-family:"Great Vibes",cursive;font-weight:400;font-size:40px;line-height:1;
    color:var(--ink);margin-bottom:12px;
  }
  .couple-names .amp{display:block;font-size:30px;margin-top:2px}
  .verse{font-size:11.5px;line-height:1.35;color:var(--ink-soft)}
  .verse b{font-weight:700}
  .date{font-size:12px;font-variant:small-caps;margin-top:7px;line-height:1.3}
  .venue{margin-top:7px;font-size:12px;line-height:1.3;font-variant:small-caps}
  .venue-name{font-weight:700;font-size:13px;font-variant:normal;text-transform:uppercase}
</style>
</head>
<body>
<main class="canvas">

  <section class="card pocket-card">
    <svg width="800" height="290" viewBox="0 0 800 290">
      <defs>
        <linearGradient id="photoWarm" x1="0" y1="0" x2="1" y2="1">
          <stop offset="0" stop-color="#c9b79d"/><stop offset="1" stop-color="#7d6a58"/>
        </linearGradient>
        <linearGradient id="photoScene" x1="0" y1="0" x2="0" y2="1">
          <stop offset="0" stop-color="#6d7d62"/><stop offset=".5" stop-color="#b69e80"/><stop offset="1" stop-color="#3a3836"/>
        </linearGradient>
        <linearGradient id="photoPortrait" x1="0" y1="0" x2="0" y2="1">
          <stop offset="0" stop-color="#d4c7b6"/><stop offset="1" stop-color="#2f3440"/>
        </linearGradient>
        <pattern id="mosaicTiles" x="14" y="222" width="144" height="58" patternUnits="userSpaceOnUse">
          <rect x="0" y="0" width="33" height="26" fill="#a58a70"/>
          <rect x="36" y="0" width="33" height="26" fill="#5f6b5a"/>
          <rect x="72" y="0" width="33" height="26" fill="#c7b299"/>
          <rect x="108" y="0" width="33" height="26" fill="#3f4656"/>
          <rect x="0" y="29" width="33" height="26" fill="#7b7f86"/>
          <rect x="36" y="29" width="33" height="26" fill="#b99878"/>
          <rect x="72" y="29" width="33" height="26" fill="#4c4a47"/>
          <rect x="108" y="29" width="33" height="26" fill="#9aa08a"/>
        </pattern>
      </defs>
      <path class="pocket-fold" d="M0 200 L520 175 L800 210" fill="none" stroke="#ffffff" stroke-opacity=".7" stroke-width="1.5"/>
      <path d="M0 202 L520 177 L800 212 V290 H0 Z" fill="#000" fill-opacity=".03"/>
      <rect class="photo-mosaic" x="14" y="222" width="771" height="55" fill="url(#mosaicTiles)" opacity=".85" role="img" aria-label="Mosaic of small photos of the couple over the years"/>
      <circle cx="245" cy="130" r="62" fill="none" stroke="var(--rim)" stroke-width="3"/>
      <circle cx="420" cy="130" r="84" fill="none" stroke="var(--rim)" stroke-width="3"/>
      <circle cx="600" cy="130" r="62" fill="none" stroke="var(--rim)" stroke-width="3"/>
      <circle cx="245" cy="130" r="55" fill="url(#photoWarm)" role="img" aria-label="Engagement portrait of the bride"/>
      <circle cx="420" cy="130" r="76" fill="url(#photoScene)" role="img" aria-label="Engagement photo of the couple sitting together outdoors"/>
      <circle cx="600" cy="130" r="55" fill="url(#photoPortrait)" role="img" aria-label="Engagement portrait of the groom"/>
    </svg>
  </section>

  <section class="card invitation-card">
    <svg width="800" height="335" viewBox="0 0 800 335">
      <defs>
        <linearGradient id="photoCouple" x1="0" y1="0" x2="1" y2="1">
          <stop offset="0" stop-color="var(--photo-dark)"/>
          <stop offset=".55" stop-color="var(--photo-warm)"/>
          <stop offset="1" stop-color="var(--photo-light)"/>
        </linearGradient>
      </defs>
      <path d="M0 0 H330 A215 215 0 0 1 330 335 H0 Z" fill="url(#photoCouple)" role="img" aria-label="Engagement photo of the couple embracing at dusk"/>
      <path d="M330 0 A215 215 0 0 1 330 335" fill="none" stroke="var(--rim)" stroke-width="3"/>
      <path d="M336 -4 A222 222 0 0 1 336 339" fill="none" stroke="var(--rim)" stroke-opacity=".6" stroke-width="1"/>
    </svg>
    <div class="invite-text">
      <h1 class="couple-names">Owen<span class="amp">&amp; Lucia</span></h1>
      <p class="verse">A life of sharing, caring<br>A love of endless going together<br>We <b>Owen</b> and <b>Lucia</b><br>Together with our parents invite you to share with us<br>As we unite our hearts in God and begin a life<br>long journey together</p>
      <p class="date">On Saturday, March 28, 2012<br>at 12:00 pm</p>
      <p class="venue"><span class="venue-name">Hillcrest Chapel</span><br>2840 Linden Ave. 14<br>Maple Grove, CA 90412</p>
    </div>
  </section>

</main>
</body>
</html>
```